Maple Lantern Business Card

Colors can be blue, grey and white as you see in the attached logo. Needs to have a spot for name, title, phone, email, address, and website. There also needs to be a spot for an agent's picture.

Contact Information for Business Card

See project description.

Colors

Designer to choose colors to be used in the design.

```html
<!DOCTYPE html>
<html lang="en">
<head>
<meta charset="utf-8">
<title>Maple Lantern Business Card</title>
<link rel="stylesheet" href="https://fonts.googleapis.com/css2?family=Montserrat:wght@400;500;700&display=swap">
<style>
  :root {
    --bg: #e9e9e9;
    --card-white: #ffffff;
    --card-dark: #2c2c2e;
    --blue: #2f6db5;
    --ink: #2b2b2b;
    --grey: #555555;
    --line: #c9c9c9;
  }
  * { box-sizing: border-box; margin: 0; padding: 0; }
  html, body { width: 1200px; height: 1051px; overflow: hidden; }
  body {
    background: var(--bg);
    font-family: "Montserrat", sans-serif;
    display: flex;
    align-items: center;
    justify-content: center;
    gap: 90px;
  }
  .card {
    width: 470px;
    height: 822px;
    border-radius: 34px;
    overflow: hidden;
    position: relative;
    box-shadow: 0 10px 30px rgba(0,0,0,0.18);
  }

  /* Front: contact side */
  .card--front {
    background: var(--card-white);
    padding: 70px 48px 0 52px;
    display: flex;
    flex-direction: column;
  }
  .agent-name {
    color: var(--blue);
    font-weight: 700;
    font-size: 46px;
    letter-spacing: 1px;
    line-height: 1;
  }
  .agent-title {
    color: var(--grey);
    font-size: 22px;
    letter-spacing: 1px;
    margin-top: 10px;
  }
  .contact-group { margin-top: 38px; }
  .contact-line {
    font-size: 19px;
    color: var(--ink);
    letter-spacing: 0.8px;
    line-height: 1.45;
  }
  .contact-line .label {
    color: var(--blue);
    font-weight: 500;
    margin-right: 6px;
  }
  .contact-line .indent { padding-left: 34px; display: block; }
  .brand {
    margin-top: auto;
    margin-bottom: 70px;
    display: flex;
    align-items: center;
    gap: 16px;
  }
  .brand-mark {
    width: 54px;
    height: 54px;
    background: var(--blue);
    flex: none;
  }
  .brand-name {
    color: var(--blue);
    font-weight: 700;
    font-size: 34px;
    letter-spacing: 1px;
    line-height: 1.1;
  }
  .brand-sub {
    display: block;
    font-size: 20px;
    letter-spacing: 6px;
  }

  /* Back: portrait side */
  .card--back { background: var(--card-dark); }
  .portrait {
    position: absolute;
    left: 0; top: 0;
    width: 100%;
    height: 610px;
    background: linear-gradient(180deg, #aab4bd 0%, #8b8580 40%, #4a4e5a 70%, #3a3d45 100%);
  }
  .back-band {
    position: absolute;
    left: 0; right: 0; bottom: 0;
    height: 212px;
    display: flex;
    flex-direction: column;
    align-items: center;
    padding-top: 34px;
  }
  .back-band .agent-name { font-size: 44px; letter-spacing: 4px; }
  .back-title {
    display: flex;
    align-items: center;
    gap: 14px;
    color: #e6e6e6;
    font-size: 20px;
    letter-spacing: 1.5px;
    margin-top: 12px;
  }
  .back-title::before, .back-title::after {
    content: "";
    width: 50px;
    height: 1.5px;
    background: var(--line);
  }
  .social-row {
    display: flex;
    gap: 16px;
    margin-top: 20px;
  }
  .social-dot {
    width: 38px;
    height: 38px;
    border-radius: 50%;
    background: var(--blue);
  }
</style>
</head>
<body>
  <section class="card card--front">
    <h1 class="agent-name">Owen Hartley</h1>
    <p class="agent-title">Relator Agent</p>

    <div class="contact-group">
      <p class="contact-line"><span class="label">C-</span>800-3147-6620</p>
      <p class="contact-line"><span class="label">F-</span>800-3148-7731</p>
    </div>
    <div class="contact-group">
      <p class="contact-line"><span class="label">W-</span>www.maplelantern.com</p>
      <p class="contact-line"><span class="label">E-</span>owen@maplelantern.com</p>
    </div>
    <div class="contact-group">
      <p class="contact-line"><span class="label">A-</span>58 Birchwood Lane, Suite 4,<span class="indent">Elmford, US 204718</span></p>
    </div>
    <div class="contact-group">
      <p class="contact-line"><span class="label">FB-</span>www.socialhub.net/maplelantern/owen</p>
      <p class="contact-line"><span class="label">T-</span>www.chirpline.net/maplelantern/owen</p>
    </div>

    <div class="brand">
      <span class="brand-mark"></span>
      <p class="brand-name">MAPLE LANTERN<span class="brand-sub">REAL ESTATE</span></p>
    </div>
  </section>

  <section class="card card--back">
    <div class="portrait" role="img" aria-label="Agent portrait in a suit seated on a rooftop terrace with a city skyline behind"></div>
    <div class="back-band">
      <h2 class="agent-name">Owen Hartley</h2>
      <p class="back-title">Relator Agent</p>
      <div class="social-row">
        <span class="social-dot"></span>
        <span class="social-dot"></span>
        <span class="social-dot"></span>
        <span class="social-dot"></span>
      </div>
    </div>
  </section>
</body>
</html>
```